Orthodontic Postcard Design for Mailing to Potential Clients - This is a redesign of an existing one

I need to modify the attached "Back To School" ai file as follows:Front Side:* Back to school - change to - Grand Opening* Excellent orthodontic care... - change to - Excellent orthodontic care for your entire family. Increasing self-esteem by creating beautiful smiles is what we do!* See why so many of your neighbors.. - change to - See why so many of your neighbors are choosing Dr. Fenwick for their family orthodontic needs.* Change address to - 4812 Calle Montoro, Suite 101Bayridge, CA 90517(858) 720-1130* Change email address to -www.Braces.CareBack Side:*
Replace "Quality can be fun... with my quote "Classic smiles are what we do!" Dr. Fenwick
Map (attached)
Eliminate current pictures - add girl with braces (attached) and my picture (attached)
Back to school... - replaced with a coupon that says Free Initial Orthodontic Consultation - Offer valid for sixty days.* Change address and websiteI would like to do these postcards every six weeks. Do you find the extra large cards more effective than the medium cards? What is the cost difference. I would like to send them to households in the 90517, 90538 and 90561 zip codes.

Target Market(s)

Typically age 7-16, and young adults

Industry/Entity Type

School

Requirements
Must have
• I need this project completed ASAP in order to send it to print.

```html
<!DOCTYPE html>
<html lang="en">
<head>
<meta charset="utf-8">
<title>Fenwick Orthodontics – Grand Opening Postcard</title>
<link rel="stylesheet" href="https://fonts.googleapis.com/css2?family=Lora:wght@400;500&family=Pinyon+Script&family=Archivo:wght@700;800&display=swap">
<style>
  :root {
    --orange: #f05a28;
    --orange-soft: #f7b896;
    --white: #ffffff;
    --ink: #111111;
    --card-edge: #c9c9c9;
    --photo-girl: linear-gradient(160deg, #7fae4a 0%, #d9b27a 45%, #f1d2b9 70%, #e58aa0 100%);
    --photo-doctor: linear-gradient(180deg, #f4f4f4 0%, #e7c6ad 35%, #2a2f3a 60%, #1f232c 100%);
  }
  * { box-sizing: border-box; margin: 0; padding: 0; }
  html, body { width: 1183px; height: 1200px; overflow: hidden; background: var(--white); }
  body { position: relative; font-family: "Lora", Georgia, serif; color: var(--ink); font-variant-numeric: lining-nums; }

  .card { position: absolute; left: 2px; width: 1178px; }
  .card-front { top: 2px; height: 586px; background: var(--white); border: 1px solid var(--card-edge); }
  .card-back { top: 606px; height: 592px; background: var(--orange); }

  .rule { position: absolute; background: var(--orange); }
  .card-back .rule { background: var(--white); }

  .headline { position: absolute; text-align: center; line-height: 1; font-weight: 400; }
  .headline .brace { display: block; font-size: 44px; }
  .headline .yourself { display: block; font-size: 46px; margin-top: -2px; }
  .headline .yourself small { font-size: 34px; }
  .headline .classic-line { display: block; margin-top: -24px; white-space: nowrap; }
  .headline .classic { font-family: "Pinyon Script", cursive; font-size: 108px; color: var(--orange); }
  .headline .smile { font-size: 60px; margin-left: -4px; }
  .card-back .headline .classic { color: var(--white); }

  .photo { position: absolute; }
  .ornament-box { position: absolute; background: var(--orange-soft); opacity: .55; }

  .practice-name { position: absolute; text-align: center; color: var(--orange); font-size: 38px; line-height: 1; }
  .practice-name span { display: block; font-size: 21px; margin-top: 4px; }
  .card-back .practice-name { color: var(--white); }

  .badge { position: absolute; border-radius: 50%; text-align: center; font-family: "Archivo", Arial, sans-serif; }
  .badge-opening { left: 662px; top: 360px; width: 168px; height: 168px; background: var(--orange); color: var(--white); border: 3px solid var(--white); box-shadow: 0 0 0 2px var(--orange); padding-top: 40px; }
  .badge-opening strong { display: block; font-size: 25px; line-height: 1; font-weight: 800; }
  .badge-opening em { display: block; font-style: normal; font-family: "Lora", Georgia, serif; font-size: 15px; line-height: 1.1; margin-top: 4px; }
  .badge-coupon { left: 60px; top: 48px; width: 196px; height: 196px; background: var(--white); color: var(--orange); padding-top: 62px; }
  .badge-coupon strong { display: block; font-size: 21px; line-height: 1.05; font-weight: 700; }
  .badge-coupon em { display: block; font-style: normal; font-family: "Lora", Georgia, serif; font-size: 13px; margin-top: 3px; }

  .contact { position: absolute; text-align: center; font-size: 15px; line-height: 1.3; color: var(--orange); }
  .visit { position: absolute; text-align: center; font-size: 18px; line-height: 1.2; color: var(--orange); }
  .card-back .contact, .card-back .visit { color: var(--white); }

  .intro { position: absolute; left: 466px; top: 226px; width: 580px; text-align: center; font-size: 18px; line-height: 1.25; }
  .neighbors { position: absolute; left: 838px; top: 332px; width: 256px; text-align: center; font-size: 18px; line-height: 1.3; color: var(--orange); }

  .story { position: absolute; left: 340px; top: 300px; width: 452px; color: var(--white); font-size: 14px; line-height: 1.25; text-align: justify; }
  .story b { font-family: "Archivo", Arial, sans-serif; font-weight: 700; font-size: 15px; }
  .story b.lead { font-size: 17px; letter-spacing: .4px; }

  .faq-q { position: absolute; left: 838px; top: 50px; width: 132px; color: var(--white); font-size: 17px; line-height: 1.1; }
  .faq-a { position: absolute; left: 838px; top: 140px; width: 152px; color: var(--white); font-size: 11px; line-height: 1.25; }
  .faq-age { position: absolute; left: 844px; top: 244px; color: var(--white); font-size: 42px; line-height: 1; }
</style>
</head>
<body>

<section class="card card-front">
  <div class="rule" style="left:29px;top:27px;width:1119px;height:3px"></div>
  <div class="rule" style="left:29px;top:560px;width:1119px;height:3px"></div>
  <div class="rule" style="left:29px;top:27px;width:3px;height:536px"></div>
  <div class="rule" style="left:1145px;top:27px;width:3px;height:536px"></div>
  <div class="rule" style="left:357px;top:27px;width:3px;height:536px"></div>
  <div class="rule" style="left:357px;top:310px;width:791px;height:3px"></div>
  <div class="rule" style="left:357px;top:452px;width:791px;height:3px"></div>
  <div class="rule" style="left:745px;top:310px;width:3px;height:144px"></div>

  <div class="photo" role="img" aria-label="Smiling teenage girl with braces" style="left:53px;top:52px;width:284px;height:424px;background:var(--photo-girl)"></div>
  <div class="ornament-box" role="img" aria-label="Decorative ornamental frame" style="left:53px;top:488px;width:284px;height:66px"></div>

  <h1 class="headline" style="left:470px;top:58px;width:620px">
    <span class="brace">Brace</span>
    <span class="yourself">Yourself <small>for a</small></span>
    <span class="classic-line"><span class="classic">Classic</span><span class="smile">Smile!</span></span>
  </h1>

  <p class="intro">Excellent orthodontic care for your entire family. Increasing self-esteem by creating beautiful smiles is what we do!</p>

  <div class="practice-name" style="left:415px;top:342px;width:270px">Fenwick<span>Orthodontics</span></div>

  <div class="badge badge-opening"><strong>GRAND<br>OPENING</strong><em>Now accepting<br>new patients.</em></div>

  <p class="neighbors">See why so many of your neighbors are choosing Dr. Fenwick for their family orthodontic needs.</p>

  <p class="contact" style="left:372px;top:484px;width:240px">4812 Calle Montoro, Suite<br>101Bayridge, CA 90517<br>(555) 314-2296</p>
  <p class="visit" style="left:904px;top:490px;width:260px">Visit Us at<br>Www.Grinly.Care</p>
</section>

<section class="card card-back">
  <div class="rule" style="left:32px;top:26px;width:1116px;height:3px"></div>
  <div class="rule" style="left:32px;top:558px;width:1116px;height:3px"></div>
  <div class="rule" style="left:32px;top:26px;width:3px;height:535px"></div>
  <div class="rule" style="left:1145px;top:26px;width:3px;height:535px"></div>
  <div class="rule" style="left:819px;top:26px;width:3px;height:535px"></div>
  <div class="rule" style="left:32px;top:278px;width:789px;height:3px"></div>
  <div class="rule" style="left:32px;top:450px;width:789px;height:3px"></div>
  <div class="rule" style="left:297px;top:278px;width:3px;height:174px"></div>
  <div class="rule" style="left:819px;top:298px;width:329px;height:3px"></div>

  <div class="badge badge-coupon"><strong>Free Initial<br>Orthodontic<br>Consultation</strong><em>Offer valid for sixty days.</em></div>

  <h2 class="headline" style="left:276px;top:76px;width:524px">
    <span class="brace">Brace</span>
    <span class="yourself">Yourself <small>for a</small></span>
    <span class="classic-line"><span class="classic">Classic</span><span class="smile">Smile!</span></span>
  </h2>

  <div class="practice-name" style="left:50px;top:322px;width:230px">Fenwick<span>Orthodontics</span></div>

  <p class="story"><b class="lead">Classic smiles are what we do!</b> At Fenwick Orthodontics, we offer more than just quality orthodontics. We offer the chance for kids to build character. We offer a fun environment – ever heard of an orthodontist with a soda fountain in his office? We offer a relaxing cafe where Mom or Dad can take a break during a hectic day. <b>That’s why, we believe, if you compare costs, you’ll come to Fenwick!</b></p>

  <p class="contact" style="left:54px;top:484px;width:220px">4812 Calle Montoro, Suite<br>101Bayridge, CA 90517<br>(555) 314-2296</p>
  <p class="visit" style="left:592px;top:488px;width:200px">Visit Us at<br>Www.Grinly.Care</p>

  <p class="faq-q">At what age should my child see an orthodontist?</p>
  <p class="faq-a">The National Orthodontic Council recommends that children be seen for an initial consultation at age</p>
  <p class="faq-age">7</p>

  <div class="photo" role="img" aria-label="Portrait of Dr. Fenwick in a suit" style="left:1006px;top:46px;width:128px;height:142px;background:var(--photo-doctor)"></div>
</section>

</body>
</html>
```